Meridale Dental Business Card

Please design a professional but colorful looking business card. Our new logo is attached. The card also needs the following information:
For ALL Your Dental Needs
Corbin T. Whitlow, D.D.S.
918-555-0147
20485-C North Larkspur, Bixby, OK 74008
www.meridaledentalexample.com

```html
<!DOCTYPE html>
<html lang="en">
<head>
<meta charset="utf-8">
<title>Meridale Dental Business Card</title>
<link href="https://fonts.googleapis.com/css2?family=Saira:wght@400;500;600&display=swap" rel="stylesheet">
<style>
  :root {
    --backdrop: #8f9091;
    --card: #f7f7f7;
    --slate: #343e43;
    --ink: #2f3336;
    --accent: #8a2e2c;
    --brand: #2a62b4;
    --on-slate: #ffffff;
  }
  * { box-sizing: border-box; margin: 0; padding: 0; }
  html, body { width: 1200px; height: 895px; overflow: hidden; }
  body {
    background: var(--backdrop);
    font-family: "Saira", sans-serif;
    position: relative;
  }
  .card {
    position: absolute;
    left: 240px;
    width: 720px;
    height: 412px;
    background: var(--card);
    overflow: hidden;
  }
  .card--front { top: 24px; }
  .card--back { top: 459px; }

  .brand {
    position: absolute;
    display: flex;
    align-items: center;
    gap: 10px;
    color: var(--brand);
    font-weight: 600;
    font-size: 24px;
    letter-spacing: 1px;
    text-transform: uppercase;
  }
  .brand__mark {
    width: 26px;
    height: 26px;
    border-radius: 50%;
    background: var(--brand);
  }
  .card--front .brand { left: 40px; top: 48px; }
  .card--back .brand { left: 50%; top: 50%; transform: translate(-50%, -50%); font-size: 30px; }

  .tab {
    position: absolute;
    right: 0;
    width: 200px;
    height: 44px;
    background: var(--slate);
  }
  .card--front .tab { top: 112px; }
  .card--back .tab { top: 100px; }

  .identity {
    position: absolute;
    left: 300px;
    top: 150px;
    text-transform: uppercase;
  }
  .identity__name {
    font-size: 32px;
    font-weight: 500;
    letter-spacing: 2px;
    color: var(--ink);
    line-height: 1.1;
  }
  .identity__name span { color: var(--accent); }
  .identity__role {
    font-size: 20px;
    letter-spacing: 3px;
    color: var(--ink);
    margin-top: 2px;
  }

  .contact-panel {
    position: absolute;
    left: 40px;
    right: 22px;
    top: 252px;
    bottom: 20px;
    background: var(--slate);
    border-radius: 22px;
    display: grid;
    grid-template-columns: 1fr 1.25fr 1fr;
    color: var(--on-slate);
  }
  .contact-item {
    display: flex;
    flex-direction: column;
    align-items: center;
    justify-content: center;
    gap: 10px;
    text-align: center;
    font-size: 14px;
    letter-spacing: 1px;
    line-height: 1.35;
    padding: 0 12px;
  }
  .contact-item + .contact-item { border-left: 1px solid var(--on-slate); }
  .contact-item svg { width: 34px; height: 34px; fill: var(--on-slate); }
</style>
</head>
<body>
  <section class="card card--front">
    <div class="brand"><span class="brand__mark"></span>Meridale Dental</div>
    <div class="tab"></div>
    <div class="identity">
      <p class="identity__name"><span>Corbin T.</span> Whitlow</p>
      <p class="identity__role">D.D.S. · For ALL Your Dental Needs</p>
    </div>
    <div class="contact-panel">
      <div class="contact-item">
        <svg viewBox="0 0 24 24" aria-hidden="true"><path d="M3 9c0-3 4-5 9-5s9 2 9 5v1.5h-5V8.5c-1.3-.6-2.6-.8-4-.8s-2.7.2-4 .8v2H3z"/><path d="M7 11.5l2-3h6l2 3 1.5 7.5h-15z"/></svg>
        <p>918-555-0147</p>
      </div>
      <div class="contact-item">
        <svg viewBox="0 0 24 24" aria-hidden="true"><path d="M12 2a10 10 0 1 0 0 20 10 10 0 0 0 0-20zm0 1.6c1.2 1.3 2.1 3.2 2.5 5.4h-5C9.9 6.8 10.8 4.9 12 3.6zM9.3 10.6h5.4a16 16 0 0 1 0 2.8H9.3a16 16 0 0 1 0-2.8zM3.7 10.6h4a18 18 0 0 0 0 2.8h-4a8.4 8.4 0 0 1 0-2.8zm12.6 0h4a8.4 8.4 0 0 1 0 2.8h-4a18 18 0 0 0 0-2.8zM4.3 9a8.4 8.4 0 0 1 5-4.6C8.6 5.7 8.1 7.3 7.9 9zm11.8 0c-.2-1.7-.7-3.3-1.4-4.6a8.4 8.4 0 0 1 5 4.6zM4.3 15h3.6c.2 1.7.7 3.3 1.4 4.6a8.4 8.4 0 0 1-5-4.6zm5.2 0h5c-.4 2.2-1.3 4.1-2.5 5.4-1.2-1.3-2.1-3.2-2.5-5.4zm6.6 0h3.6a8.4 8.4 0 0 1-5 4.6c.7-1.3 1.2-2.9 1.4-4.6z"/></svg>
        <p>hello@meridaledentalexample.com<br>www.meridaledentalexample.com</p>
      </div>
      <div class="contact-item">
        <svg viewBox="0 0 24 24" aria-hidden="true"><path d="M12 1.5a7 7 0 0 0-7 7c0 5 7 14 7 14s7-9 7-14a7 7 0 0 0-7-7zm0 4a3 3 0 1 1 0 6 3 3 0 0 1 0-6z"/></svg>
        <p>20485-C North Larkspur,<br>Bixby, OK 74008</p>
      </div>
    </div>
  </section>

  <section class="card card--back">
    <div class="brand"><span class="brand__mark"></span>Meridale Dental</div>
    <div class="tab"></div>
  </section>
</body>
</html>
```